Harrowgate Estates Business Card for Apartment Buildings

Create business cards for resident managers who run apartment buildings. The audience is the public who are searching for apartment rentals, and current residents who live at the apartment building. Key design element will be incorporating the company logo, however, the logo cannot dominate. The building name and manager name are more important than the logo. Current business card design leaves little room for copy, so we may need to reduce the size on the current card to allow for more space for copy.

Target Market(s)

Adults 18-65 years of age, who are looking for an apartment rental, plus current residents who live at our apartment buildings.

Industry/Entity Type

Property Management

Contact Information for Business Card

A major design element will be use of the company logo. Important property and manager contact information must be part of the design. The size of the logo will need to be reduced to make room for building and manager contact copy.

Font styles to use
Sans Serif

Colors
3176b5
000000
959595
ffffff

Requirements
Must have
• 1) Incorporate the company logo.
• 2) Use the company colors (dark blue, black/grey, over white).
• 3) FEATURE THE BUILDING NAME
• 4) FEATURE THE MANAGER NAME
• 5) The company name is less important than BUILDING and MANAGER
• 6) Manager contact information
• **SEE ATTACHED CREATIVE BRIEF**
Nice to have
• 1) Back of card logo watermark
• 2) Ability to write notes on back of carfd
Should not have
• Avoid letting the company logo dominate the card, the building name and manager are more important than the company logo.

```html
<!DOCTYPE html>
<html lang="en">
<head>
<meta charset="utf-8">
<title>Harrowgate Estates – Resident Manager Business Cards</title>
<link href="https://fonts.googleapis.com/css2?family=Arimo:wght@400;700&family=Roboto+Condensed:wght@700&display=swap" rel="stylesheet">
<style>
  :root {
    --brand-blue: #0b6aa8;
    --ink-blue: #2166a8;
    --charcoal: #48484a;
    --paper: #ffffff;
    --backdrop: #ececec;
    --rule-light: #d9d9d9;
    --mark-faint: #ececf2;
    --mark-faint-dark: #545456;
  }
  * { margin: 0; padding: 0; box-sizing: border-box; }
  html, body { width: 1200px; height: 900px; overflow: hidden; }
  body {
    background: var(--backdrop);
    font-family: "Arimo", Arial, sans-serif;
    position: relative;
  }
  .card {
    position: absolute;
    width: 508px;
    height: 297px;
    overflow: hidden;
  }
  .card--front-top { left: 89px; top: 92px; }
  .card--back-top { left: 617px; top: 94px; width: 499px; height: 292px; background: var(--paper); }
  .card--front-bottom { left: 89px; top: 473px; }
  .card--back-bottom { left: 617px; top: 478px; width: 499px; height: 292px; background: var(--charcoal); }

  .front-panel { position: absolute; inset: 0; }

  .company-name {
    position: absolute;
    left: 25px; top: 28px;
    color: var(--paper);
    font-weight: 700;
    text-transform: uppercase;
  }
  .company-name__main {
    display: block;
    font-size: 30px;
    line-height: 32px;
  }
  .company-name__sub {
    display: block;
    font-size: 13px;
    line-height: 16px;
    letter-spacing: 5.5px;
  }
  .manager-name {
    position: absolute;
    left: 25px; top: 88px;
    font-family: "Roboto Condensed", "Arial Narrow", sans-serif;
    font-weight: 700;
    font-size: 20px;
    color: var(--paper);
    text-transform: uppercase;
  }
  .manager-title {
    position: absolute;
    left: 26px; top: 110px;
    font-size: 13.5px;
    color: var(--paper);
  }
  .building-address {
    position: absolute;
    left: 24px; top: 138px;
    font-size: 12.5px;
    line-height: 15.5px;
    color: var(--paper);
    font-style: normal;
  }
  .building-name { display: block; }
  .contact-list {
    position: absolute;
    left: 26px; top: 190px;
    list-style: none;
    font-size: 12.5px;
    line-height: 16px;
    color: var(--paper);
  }
  .brand-spot {
    position: absolute;
    left: 300px; top: 138px;
    width: 190px;
    display: flex;
    align-items: center;
    gap: 8px;
  }
  .brand-spot__dot {
    width: 16px; height: 16px;
    border-radius: 50%;
    background: var(--brand-blue);
    flex: none;
  }
  .brand-spot__name {
    font-weight: 700;
    font-size: 19px;
    line-height: 22px;
    color: var(--charcoal);
    text-transform: uppercase;
  }

  .notes-watermark {
    position: absolute;
    left: 225px; top: 115px;
    font-weight: 700;
    font-size: 30px;
    line-height: 34px;
    text-transform: uppercase;
    color: var(--mark-faint);
  }
  .card--back-bottom .notes-watermark { color: var(--mark-faint-dark); }
  .notes-label {
    position: absolute;
    left: 45px; top: 34px;
    font-size: 15.5px;
    color: var(--ink-blue);
  }
  .card--back-bottom .notes-label { color: var(--paper); }
  .notes-lines { position: absolute; left: 45px; top: 0; width: 413px; height: 100%; }
  .notes-lines line { stroke: var(--ink-blue); stroke-width: 1; }
  .card--back-bottom .notes-lines line { stroke: var(--rule-light); }
</style>
</head>
<body>

  <!-- Front, upper -->
  <section class="card card--front-top">
    <svg class="front-panel" width="508" height="297" viewBox="0 0 508 297">
      <rect width="508" height="297" fill="var(--brand-blue)"/>
      <rect x="398" width="110" height="297" fill="var(--paper)"/>
      <circle cx="389" cy="160" r="155" fill="var(--paper)"/>
    </svg>
    <p class="company-name">
      <span class="company-name__main">Harrowgate</span>
      <span class="company-name__sub">Estates</span>
    </p>
    <h2 class="manager-name">Marisol Quintero</h2>
    <p class="manager-title">Resident Manager</p>
    <address class="building-address">
      <span class="building-name">Linden Court Apartments</span>
      2485 Bramble Avenue<br>
      Westbrook, CA 92418
    </address>
    <ul class="contact-list">
      <li>Phone 555-214-3380</li>
      <li>Fax 555-214-3381</li>
      <li>Cell 555-867-4102</li>
      <li>marisol@harrowgate.com</li>
      <li>www.harrowgateestates.com</li>
    </ul>
    <div class="brand-spot">
      <span class="brand-spot__dot"></span>
      <span class="brand-spot__name">Harrowgate Estates</span>
    </div>
  </section>

  <!-- Back, white -->
  <section class="card card--back-top">
    <p class="notes-watermark">Harrowgate<br>Estates</p>
    <p class="notes-label">Write Notes:</p>
    <svg class="notes-lines" viewBox="0 0 413 292" width="413" height="292">
      <line x1="0" y1="77" x2="413" y2="77"/>
      <line x1="0" y1="104" x2="413" y2="104"/>
      <line x1="0" y1="131" x2="413" y2="131"/>
      <line x1="0" y1="158" x2="413" y2="158"/>
      <line x1="0" y1="185" x2="413" y2="185"/>
      <line x1="0" y1="212" x2="413" y2="212"/>
      <line x1="0" y1="239" x2="413" y2="239"/>
    </svg>
  </section>

  <!-- Front, lower -->
  <section class="card card--front-bottom">
    <svg class="front-panel" width="508" height="297" viewBox="0 0 508 297">
      <rect width="508" height="297" fill="var(--brand-blue)"/>
      <rect x="398" width="110" height="297" fill="var(--paper)"/>
      <circle cx="389" cy="160" r="155" fill="var(--paper)"/>
    </svg>
    <p class="company-name">
      <span class="company-name__main">Harrowgate</span>
      <span class="company-name__sub">Estates</span>
    </p>
    <h2 class="manager-name">Marisol Quintero</h2>
    <p class="manager-title">Resident Manager</p>
    <address class="building-address">
      <span class="building-name">Linden Court Apartments</span>
      2485 Bramble Avenue<br>
      Westbrook, CA 92418
    </address>
    <ul class="contact-list">
      <li>Phone 555-214-3380</li>
      <li>Fax 555-214-3381</li>
      <li>Cell 555-867-4102</li>
      <li>marisol@harrowgate.com</li>
      <li>www.harrowgateestates.com</li>
    </ul>
    <div class="brand-spot">
      <span class="brand-spot__dot"></span>
      <span class="brand-spot__name">Harrowgate Estates</span>
    </div>
  </section>

  <!-- Back, charcoal -->
  <section class="card card--back-bottom">
    <p class="notes-watermark">Harrowgate<br>Estates</p>
    <p class="notes-label">Write Notes:</p>
    <svg class="notes-lines" viewBox="0 0 413 292" width="413" height="292">
      <line x1="0" y1="77" x2="413" y2="77"/>
      <line x1="0" y1="104" x2="413" y2="104"/>
      <line x1="0" y1="131" x2="413" y2="131"/>
      <line x1="0" y1="158" x2="413" y2="158"/>
      <line x1="0" y1="185" x2="413" y2="185"/>
      <line x1="0" y1="212" x2="413" y2="212"/>
      <line x1="0" y1="239" x2="413" y2="239"/>
    </svg>
  </section>

</body>
</html>
```